we are an outdoor outlet in a country club that has a variety of outlets. The Club is called Nilevane and is located in Cairo, Egypt. This garden menu will include cuisines from the Mediterranean, Asia and Texmex. we need a menu that is colorful and would fit an A3 size, back and front are to be used. Attached is the old menu currently in use (Garden Menu 2012.pdf is just for reference) and the new menu text for you to use is under the name Garden Menu Fall 2013
thank you.

```html
<!DOCTYPE html>
<html lang="en">
<head>
<meta charset="utf-8">
<title>Nilevane Country Club – Garden Menu</title>
<link rel="stylesheet" href="https://fonts.googleapis.com/css2?family=Raleway:wght@300;400&family=Josefin+Sans:wght@600&family=Bitter:wght@600&display=swap">
<style>
:root{
  --red:#9a1a1e;
  --green:#1f5b3b;
  --pink:#d8006a;
  --yellow:#f6ea1c;
  --blue:#2b8fd8;
  --badge:#1b8ddb;
  --orange:#e0591d;
  --shadow:#3b1a12;
  --white:#ffffff;
  --rule:rgba(255,255,255,.75);
}
*{margin:0;padding:0;box-sizing:border-box}
html,body{width:1200px;height:848px;overflow:hidden;background:#fff}
.menu{position:relative;width:1200px;height:848px;overflow:hidden;font-family:"Raleway",sans-serif;color:var(--white)}
.panel{position:absolute;top:0;height:848px}
.panel--asian{left:0;width:400px;background:var(--red)}
.panel--center{left:400px;width:400px;background:var(--green)}
.panel--desserts{left:800px;width:400px;background:var(--pink)}

.photo{position:absolute}
.photo--stirfry{left:0;top:0;width:400px;height:234px;background:radial-gradient(circle at 45% 45%,#5a3522 0,#7a4a2c 22%,#d9d4cc 48%,#f1efeb 75%)}
.photo--tacos{left:0;top:304px;width:400px;height:270px;background:radial-gradient(ellipse at 45% 60%,#e2b15c 0,#c9783a 28%,#c0412f 55%,#8f9c6a 85%)}
.photo--fondant{left:0;top:0;width:400px;height:249px;background:radial-gradient(circle at 52% 35%,#5a2d1c 0,#7b3d24 16%,#e7e4e2 34%,#fbfbfb 70%)}

.banner{position:absolute;font-family:"Raleway",sans-serif;font-weight:400;line-height:1;white-space:nowrap;overflow:hidden}
.banner--asian{left:0;top:176px;width:300px;height:34px;background:var(--green);font-size:30px;padding-left:70px;padding-top:2px}
.banner--texmex{left:0;top:304px;width:157px;height:33px;background:var(--red);font-size:28px;padding-left:32px;padding-top:3px}
.banner--desserts{left:0;top:221px;width:300px;height:33px;background:var(--yellow);color:var(--blue);font-size:26px;padding-left:165px;padding-top:4px}
.fold{position:absolute}

.heading{position:absolute;left:0;width:100%;text-align:center;font-family:"Josefin Sans",sans-serif;font-weight:600;line-height:1}
.heading--main{font-size:24px;letter-spacing:6.5px}
.heading--section{font-size:19px;letter-spacing:5px}
.divider{position:absolute;height:1px;background:var(--rule)}
.divider::after{content:"";position:absolute;left:50%;top:-11px;width:22px;height:22px;margin-left:-11px;border-radius:50%;background:var(--white)}

.item{position:absolute}
.item__name{display:block;font-size:12.5px;font-weight:400;line-height:14px;text-transform:uppercase;letter-spacing:.2px}
.item__name--plain{text-transform:none}
.item__price{position:absolute;right:0;top:0;font-size:12.5px;line-height:14px}
.item__desc{font-family:"Bitter",serif;font-weight:600;font-size:9.3px;line-height:12.3px}

.panel--asian .item{left:57px;width:286px}
.panel--center .item{left:54px;width:284px}
.panel--desserts .item{left:55px;width:283px}
.panel--desserts .item__name{font-weight:300}

.brand{position:absolute;left:48px;top:730px;white-space:nowrap;font-family:"Raleway",sans-serif;font-weight:400;color:var(--white);line-height:1}
.brand__name{display:block;font-size:31px}
.brand__tag{display:block;font-size:11px;letter-spacing:3.5px;margin-top:5px;padding-left:50px}

.notice{position:absolute;left:261px;top:716px;width:98px;height:98px;border-radius:50%;background:var(--badge);border:3px solid var(--white);box-shadow:0 0 0 2px var(--badge);display:flex;align-items:center;justify-content:center;text-align:center;font-family:"Bitter",serif;font-weight:600;font-size:8.3px;line-height:9.6px}
</style>
</head>
<body>
<div class="menu">

  <section class="panel panel--asian">
    <div class="photo photo--stirfry" role="img" aria-label="Photo of beef stir-fry with peppers, rice and chopsticks on a white plate"></div>
    <div class="banner banner--asian">ASIAN CORNER</div>
    <svg class="fold" style="left:272px;top:210px" width="28" height="32" viewBox="0 0 28 32"><polygon points="0,0 28,0 0,32" fill="var(--shadow)"/></svg>

    <h2 class="heading heading--main" style="top:263px">main courses</h2>
    <div class="divider" style="left:57px;width:286px;top:302px"></div>

    <div class="item" style="top:326px"><span class="item__name">Murgh Chicken Makhni</span><span class="item__price">00.00</span>
      <p class="item__desc">Chicken cubes in a rich creamy tomato sauce<br>seasoned with garam masala<br>Choice of side: vegetable korma or curd</p></div>
    <div class="item" style="top:389px"><span class="item__name">Chicken Tandoori</span><span class="item__price">00.00</span>
      <p class="item__desc">Grilled chicken cubes with tandoori spices<br>served with basmati rice</p></div>
    <div class="item" style="top:439px"><span class="item__name">Thai Coconut Curry Shrimp</span><span class="item__price">00.00</span>
      <p class="item__desc">Sautéed shrimp tossed with curry<br>and coconut milk served with jasmine rice</p></div>
    <div class="item" style="top:489px"><span class="item__name">Mongolian Beef</span><span class="item__price">00.00</span>
      <p class="item__desc">Soy marinated beef with oyster sauce<br>and vegetables served with egg noodles</p></div>

    <h2 class="heading heading--section" style="top:553px">salads &amp; appetizer</h2>
    <div class="divider" style="left:57px;width:286px;top:588px"></div>

    <div class="item" style="top:611px"><span class="item__name">Chicken Wasabi Salad</span><span class="item__price">00.00</span>
      <p class="item__desc">Diced chicken with a mayo wasabi<br>dressing on top of shredded lettuce</p></div>
    <div class="item" style="top:661px"><span class="item__name">Chicken Sesame Noodle Salad</span><span class="item__price">00.00</span>
      <p class="item__desc">Sesame crusted chicken with glass noodles<br>tossed with sweet chili, soy sauce, and lemongrass</p></div>
    <div class="item" style="top:712px"><span class="item__name">Spring Rolls</span><span class="item__price">00.00</span>
      <p class="item__desc">Vegetable spring rolls served with house made<br>sweet and sour dip</p></div>
    <div class="item" style="top:762px"><span class="item__name">Indian Samosa</span><span class="item__price">00.00</span>
      <p class="item__desc">Fried dough parcels filled with<br>vegetables and spices</p></div>
  </section>

  <section class="panel panel--center">
    <h2 class="heading heading--main" style="top:36px;line-height:25px">main courses<br>&amp; sandwiches</h2>
    <div class="divider" style="left:54px;width:284px;top:100px"></div>

    <div class="item" style="top:114px"><span class="item__name item__name--plain">Cheeseburger</span><span class="item__price">00.00</span>
      <p class="item__desc">House made lean beef burger<br>topped with cheddar cheese</p></div>
    <div class="item" style="top:164px"><span class="item__name item__name--plain">Mushroom Burger</span><span class="item__price">00.00</span>
      <p class="item__desc">Beef burger with sautéed mushroom,<br>caramelized onion, and provolone cheese</p></div>
    <div class="item" style="top:214px"><span class="item__name item__name--plain">Crispy Chicken Wrap</span><span class="item__price">00.00</span>
      <p class="item__desc">Crisp fried chicken wrap with a ranch dressing</p></div>
    <div class="item" style="top:253px"><span class="item__name item__name--plain">Fajita (Chicken, Beef, Combo)</span><span class="item__price">00.00</span>
      <p class="item__desc">Pan seared meat or chicken with onion and<br>bell pepper served with sour cream, guacamole, salsa</p></div>

    <div class="photo photo--tacos" role="img" aria-label="Photo of grilled chicken tacos with salsa dishes on a checked tablecloth"></div>
    <div class="banner banner--texmex">TEX MEX</div>
    <svg class="fold" style="left:128px;top:337px" width="29" height="30" viewBox="0 0 29 30"><polygon points="0,0 29,0 29,30" fill="var(--shadow)"/></svg>

    <h2 class="heading heading--section" style="top:583px">salads &amp; appetizer</h2>
    <div class="divider" style="left:54px;width:284px;top:617px"></div>

    <div class="item" style="top:635px"><span class="item__name">Caesar Salad</span><span class="item__price">00.00</span>
      <p class="item__desc">Iceberg lettuce with Caesar dressing with<br>grated Parmesan cheese and croutons</p></div>
    <div class="item" style="top:685px"><span class="item__name">Taco Salad 42</span><span class="item__price">00.00</span>
      <p class="item__desc">Chicken breast, beans, sour cream, guacamole,<br>tomato, corn, lettuce, olives, chives, vinaigrette</p></div>
    <div class="item" style="top:736px"><span class="item__name">Nachos</span><span class="item__price">00.00</span>
      <p class="item__desc">Topped with chili, melted cheese, beans</p></div>
    <div class="item" style="top:774px"><span class="item__name">Chicken Quesadilla</span><span class="item__price">00.00</span>
      <p class="item__desc">served with guacamole, salsa, and sour cream</p></div>
  </section>

  <section class="panel panel--desserts">
    <div class="photo photo--fondant" role="img" aria-label="Photo of chocolate fondant with strawberries and berries on a white plate"></div>
    <div class="banner banner--desserts">DESSERTS</div>
    <svg class="fold" style="left:272px;top:254px" width="28" height="34" viewBox="0 0 28 34"><polygon points="0,0 28,0 0,34" fill="var(--orange)"/></svg>

    <div class="item" style="top:267px"><span class="item__name">Mix Berries Cheesecake</span><span class="item__price">00.00</span></div>
    <div class="item" style="top:296px"><span class="item__name">Crème Brulee</span><span class="item__price">00.00</span></div>
    <div class="item" style="top:325px"><span class="item__name">Chocolate Caramel Cake</span><span class="item__price">00.00</span></div>
    <div class="item" style="top:354px"><span class="item__name">Warm Chocolate Fondant</span><span class="item__price">00.00</span></div>
    <div class="item" style="top:383px"><span class="item__name">Baked Apple Tart Tatin</span><span class="item__price">00.00</span></div>
    <div class="item" style="top:412px"><span class="item__name">Tiramisu</span><span class="item__price">00.00</span></div>
    <div class="item" style="top:441px"><span class="item__name">Pumpkin Pie Flan</span><span class="item__price">00.00</span></div>
    <div class="item" style="top:470px"><span class="item__name">Mixed Berries Granola Yoghurt</span><span class="item__price">00.00</span></div>
    <div class="item" style="top:499px"><span class="item__name">Vanilla Ice Cream</span><span class="item__price">00.00</span>
      <p class="item__desc">Profiterole with dark and white chocolate sauce</p></div>
    <div class="item" style="top:540px"><span class="item__name">Caramelized Banana</span><span class="item__price">00.00</span>
      <p class="item__desc">With deep fried ice cream</p></div>
    <div class="item" style="top:581px"><span class="item__name">Baklava</span><span class="item__price">00.00</span>
      <p class="item__desc">With nuts and sugar syrup</p></div>
    <div class="item" style="top:622px"><span class="item__name">Shot Glass Sampler</span><span class="item__price">00.00</span>
      <p class="item__desc">Tiramisu, chocolate crisp mousse,<br>pear with sabayon</p></div>
    <div class="item" style="top:674px"><span class="item__name">Ice Cream by Scoop</span><span class="item__price">00.00</span></div>

    <div class="brand"><span class="brand__name">Nilevane</span><span class="brand__tag">country club</span></div>
    <div class="notice">PRICES ARE<br>SUBJECT TO<br>12% SERVICE<br>CHARGE &amp;<br>10% SALES TAX</div>
  </section>

</div>
</body>
</html>
```